Mondaxe custom business card design

Need a authentic, innovative business card design for a new mobile app business. I am uploading a few screen images from our app for you to view. I would like app design theme to match business card design. I can also send logo images.

```html
<!DOCTYPE html>
<html lang="en">
<head>
<meta charset="utf-8">
<title>Mondaxe Business Card</title>
<link rel="stylesheet" href="https://fonts.googleapis.com/css2?family=Open+Sans:wght@400;600;700;800&display=swap">
<style>
  :root {
    --backdrop: #d9d6d2;
    --card-black: #232323;
    --card-black-emboss: #2e2e2e;
    --card-black-shadow: #181818;
    --card-white: #f3f2ef;
    --brand-purple: #6a2bb0;
    --ink: #1d1d1d;
    --ink-soft: #3a3a3a;
  }
  * { box-sizing: border-box; margin: 0; padding: 0; }
  html, body {
    width: 1200px; height: 672px; overflow: hidden;
    background: var(--backdrop);
    font-family: "Open Sans", Arial, sans-serif;
  }
  .canvas {
    width: 1200px; height: 672px;
    display: flex; align-items: center; justify-content: center; gap: 40px;
  }
  .card {
    width: 480px; height: 274px; position: relative; overflow: hidden;
    box-shadow: 0 10px 24px rgba(0,0,0,.22);
  }

  /* Front: black card */
  .card--front { background: var(--card-black); }
  .front-brand {
    position: absolute; left: 48px; top: 0; bottom: 0;
    display: flex; flex-direction: column; align-items: flex-start; justify-content: center; gap: 14px;
  }
  .front-brand__dot {
    width: 72px; height: 72px; border-radius: 50%; background: var(--brand-purple);
  }
  .front-brand__name {
    font-weight: 800; font-size: 34px; letter-spacing: .5px;
    color: var(--card-black-emboss);
    text-shadow: 0 1px 0 #3a3a3a, 0 -1px 0 var(--card-black-shadow);
  }
  .front-emboss {
    position: absolute; right: 34px; top: 26px; width: 222px; height: 222px; border-radius: 50%;
    border: 2px solid var(--card-black-emboss);
    box-shadow: inset 0 1px 0 #353535, 0 1px 0 var(--card-black-shadow);
  }

  /* Back: white card */
  .card--back { background: var(--card-white); }
  .back-brand {
    position: absolute; left: 40px; top: 0; bottom: 0; width: 150px;
    display: flex; flex-direction: column; align-items: center; justify-content: center; gap: 10px;
  }
  .back-brand__dot {
    width: 64px; height: 64px; border-radius: 50%; background: var(--brand-purple);
  }
  .back-brand__name {
    font-weight: 800; font-size: 24px; color: var(--ink);
  }
  .back-divider {
    position: absolute; left: 212px; top: 44px; width: 2px; height: 186px;
    background: var(--brand-purple); opacity: .8;
  }
  .back-details {
    position: absolute; left: 236px; top: 40px;
  }
  .person-name { font-weight: 700; font-size: 24px; color: var(--ink); line-height: 1.1; }
  .person-title { font-size: 14px; color: var(--brand-purple); margin-top: 4px; }
  .contact-list { list-style: none; margin-top: 22px; display: grid; gap: 9px; }
  .contact-list li {
    display: flex; align-items: center; gap: 12px;
    font-size: 14px; color: var(--ink-soft);
  }
  .contact-list svg { width: 14px; height: 14px; flex: none; }
</style>
</head>
<body>
<main class="canvas">
  <section class="card card--front" aria-label="Card front">
    <div class="front-brand">
      <span class="front-brand__dot"></span>
      <span class="front-brand__name">Mondaxe</span>
    </div>
    <div class="front-emboss"></div>
  </section>

  <section class="card card--back" aria-label="Card back">
    <div class="back-brand">
      <span class="back-brand__dot"></span>
      <span class="back-brand__name">Mondaxe</span>
    </div>
    <div class="back-divider"></div>
    <div class="back-details">
      <p class="person-name">Your Name</p>
      <p class="person-title">Job Title</p>
      <ul class="contact-list">
        <li>
          <svg viewBox="0 0 14 14" aria-hidden="true"><rect x="3.5" y="1" width="7" height="12" rx="1.5" fill="none" stroke="#6a2bb0" stroke-width="1.4"/></svg>
          000 000 0000
        </li>
        <li>
          <svg viewBox="0 0 14 14" aria-hidden="true"><rect x="1" y="3" width="12" height="8.5" fill="#6a2bb0"/><path d="M1 3l6 5 6-5" fill="none" stroke="#f3f2ef" stroke-width="1.2"/></svg>
          youremail@xyz.com
        </li>
        <li>
          <svg viewBox="0 0 14 14" aria-hidden="true"><g fill="none" stroke="#6a2bb0" stroke-width="1.2"><circle cx="7" cy="7" r="6"/><ellipse cx="7" cy="7" rx="2.6" ry="6"/><path d="M1 7h12M2 4h10M2 10h10"/></g></svg>
          www.yourwebsite.com
        </li>
      </ul>
    </div>
  </section>
</main>
</body>
</html>
```